Modern Spot UV Business Card design

We are a relatively new real estate agency. We need a business card that reflects the professionalism and prestige of our company but is also modern and fresh, based around our logo.
We would love to utilise spot UV.
Happy to let the designers use their imagination and see what they come up with (we're not very creative, so have no ideas for you, sorry) :-)
We'd like one for each staff member, but I've just provided one staff members photo here to avoid confusion.

Target Market(s)

Families

Industry/Entity Type

Real Estate Agent

Contact Information for Business Card

Dale Verco - Director & Principal
Mobile: 0491 627 540
Email: dale.verco@vbrokers.example.au
Phone: (08) 8374 6150
Fax: (08) 8374 6198
www.vercobrokersproperty.example.au

Font styles to use
Other font styles liked:
• Kabel Dm BT

Requirements
Must have
• Contact details, logo, photo, spot UV
Nice to have
• Modern interesting features that will make people comment. Nothing too feminine nor too masculine.
Should not have
• No houses! Nothing typical of a real estate agent.

```html
<!DOCTYPE html>
<html lang="en">
<head>
<meta charset="utf-8">
<title>Verco Brokers Property – Business Card</title>
<link href="https://fonts.googleapis.com/css2?family=Cinzel:wght@400;700&family=Open+Sans:wght@400;600;700&display=swap" rel="stylesheet">
<style>
  :root {
    --page-bg: #1c1c1c;
    --card-white: #ffffff;
    --card-facet: #eceef0;
    --ink-dark: #3a3a3a;
    --ink-mid: #555555;
    --accent-blue: #2a8fd6;
    --back-bg: #2a2a2a;
    --uv-black: #141414;
    --uv-sheen: #3c3c3c;
    --skyline: #222222;
    --service-ink: #4a4a4a;
  }
  * { margin: 0; padding: 0; box-sizing: border-box; }
  html, body { width: 1200px; height: 873px; overflow: hidden; }
  body {
    background: var(--page-bg);
    font-family: "Open Sans", Arial, sans-serif;
    position: relative;
  }
  .card {
    position: absolute;
    width: 540px;
    height: 310px;
    border-radius: 3px;
    overflow: hidden;
    box-shadow: 0 10px 30px rgba(0,0,0,.6);
  }
  /* Front */
  .card-front {
    left: 45px; top: 280px;
    background: linear-gradient(135deg, var(--card-white) 0%, var(--card-facet) 55%, var(--card-white) 100%);
  }
  .portrait {
    position: absolute;
    right: 0; top: 0;
    width: 300px; height: 230px;
    background: radial-gradient(ellipse at 55% 70%, #5a6068 0%, #7d838a 40%, #f4f4f4 75%, #ffffff 100%);
  }
  .brand {
    position: absolute;
    left: 30px; top: 118px;
    display: flex; align-items: center; gap: 10px;
  }
  .brand-dot {
    width: 22px; height: 22px; border-radius: 50%;
    background: var(--accent-blue);
  }
  .brand-name {
    font-size: 22px; font-weight: 700; color: var(--ink-dark);
    letter-spacing: -0.3px; line-height: 1;
  }
  .tagline {
    position: absolute;
    left: 62px; top: 148px;
    font-size: 10px; color: var(--ink-mid);
  }
  .contacts {
    position: absolute;
    left: 30px; top: 200px;
    list-style: none;
  }
  .contacts li {
    display: flex; align-items: center; gap: 10px;
    font-size: 13px; color: var(--ink-dark);
    height: 22px;
  }
  .contacts svg { width: 13px; height: 13px; fill: var(--accent-blue); flex: none; }
  /* Back */
  .card-back {
    left: 615px; top: 280px;
    background: var(--back-bg);
  }
  .headline {
    position: absolute;
    left: 0; right: 0; top: 40px;
    text-align: center;
    font-family: "Cinzel", "Times New Roman", serif;
    color: var(--uv-black);
    text-shadow: 0 1px 0 var(--uv-sheen);
    line-height: 1.05;
  }
  .headline .line-sm { display: block; font-size: 30px; letter-spacing: 3px; }
  .headline .line-lg { display: block; font-size: 50px; font-weight: 700; letter-spacing: 6px; }
  .skyline {
    position: absolute;
    left: 0; right: 0; bottom: 0;
    height: 150px;
    background: linear-gradient(to top, var(--skyline) 0%, var(--skyline) 60%, rgba(34,34,34,0) 100%);
  }
  .services {
    position: absolute;
    left: 0; right: 0; bottom: 28px;
    display: flex; justify-content: center; gap: 26px;
    font-family: "Cinzel", "Times New Roman", serif;
    font-size: 14px; letter-spacing: 2px;
    color: var(--service-ink);
  }
  .services .divider { color: #777; }
</style>
</head>
<body>
  <section class="card card-front">
    <div class="portrait" role="img" aria-label="Portrait photograph of the agent in a suit"></div>
    <div class="brand">
      <span class="brand-dot"></span>
      <span class="brand-name">Verco Brokers Property</span>
    </div>
    <p class="tagline">Helping you make your next move</p>
    <ul class="contacts">
      <li><svg viewBox="0 0 16 16"><path d="M3 1l3 0 1 4-2 1c1 2 3 4 5 5l1-2 4 1 0 3c0 1-1 2-2 2C6 15 1 10 1 3c0-1 1-2 2-2z"/></svg>(08) 8374 6150</li>
      <li><svg viewBox="0 0 16 16"><path d="M4 0h8v16H4zM5.5 2v10h5V2z"/></svg>0491 627 540</li>
      <li><svg viewBox="0 0 16 16"><path d="M4 1h8v4H4zM1 6h14v7h-3v2H4v-2H1zM5 11v3h6v-3z"/></svg>(08) 8374 6198</li>
      <li><svg viewBox="0 0 16 16"><path d="M0 3h16v10H0zM1.5 4.5L8 9l6.5-4.5z"/></svg>dale.verco@vbrokers.example.au</li>
    </ul>
  </section>

  <section class="card card-back">
    <h1 class="headline">
      <span class="line-sm">Looking for</span>
      <span class="line-lg">Best Deals</span>
      <span class="line-sm">in Property ?</span>
    </h1>
    <div class="skyline" role="img" aria-label="City skyline silhouette in spot UV"></div>
    <p class="services">
      <span>Buying</span><span class="divider">|</span>
      <span>Selling</span><span class="divider">|</span>
      <span>Renting</span>
    </p>
  </section>
</body>
</html>
```